Accounting firm for Dentists needs a brochure

We are an accounting firm that specializes in dental practices. We have the information we want attached in a word file. We don't care the number of folds. We would just like it to look professional. Our logo is also attached so you know what our company colors are.

Industry/Entity Type

Accounting

```html
<!DOCTYPE html>
<html lang="en">
<head>
<meta charset="utf-8">
<title>Crestline Dental CPAs Ltd. – Tri-fold Brochure</title>
<link href="https://fonts.googleapis.com/css2?family=Cinzel:wght@700&family=Questrial&family=Open+Sans:wght@400;700&display=swap" rel="stylesheet">
<style>
  :root {
    --stage: #3b3d40;
    --paper-top: #ffffff;
    --aqua-soft: #dcf3f8;
    --aqua-mid: #93dcec;
    --aqua-deep: #45bfd9;
    --ink: #141c22;
    --ink-strong: #0a1014;
    --brand-blue: #2e9fd6;
    --brand-grey: #6a6f74;
  }
  * { box-sizing: border-box; margin: 0; padding: 0; }
  html, body {
    width: 1200px; height: 1020px; overflow: hidden;
    background: var(--stage);
  }
  .canvas {
    position: relative; width: 1200px; height: 1020px;
  }
  .spread {
    position: absolute; display: flex;
    box-shadow: 0 10px 28px rgba(0,0,0,.45);
  }
  .spread--inside { left: 60px; top: 40px; }
  .spread--outside { left: 240px; top: 530px; }
  .panel {
    position: relative; width: 360px; height: 460px; overflow: hidden;
    padding: 26px 30px;
    font-family: "Questrial", "Open Sans", sans-serif;
    color: var(--ink); font-size: 14.5px; line-height: 1.42;
    background:
      radial-gradient(circle at 85% 35%, rgba(255,255,255,.45) 0 110px, transparent 112px),
      radial-gradient(circle at 10% 80%, rgba(255,255,255,.28) 0 150px, transparent 152px),
      linear-gradient(180deg, var(--paper-top) 0%, var(--aqua-soft) 28%, var(--aqua-mid) 68%, var(--aqua-deep) 100%);
  }
  .panel + .panel { border-left: 1px solid rgba(255,255,255,.55); }
  .panel-title {
    font-family: "Cinzel", serif; font-weight: 700; font-size: 19px;
    text-align: center; color: var(--ink-strong); margin-bottom: 14px;
    letter-spacing: .5px;
  }
  .section-title {
    font-family: "Open Sans", sans-serif; font-weight: 700; font-size: 14px;
    text-align: center; text-transform: uppercase; letter-spacing: .6px;
    color: var(--ink-strong); margin: 14px 0 4px;
  }
  .section-text { text-align: justify; hyphens: auto; }
  .section + .section { margin-top: 26px; }

  /* Cover */
  .cover { padding: 0; }
  .cover-logo {
    display: flex; align-items: center; gap: 10px;
    margin: 26px 30px 0; padding: 22px 18px;
    background: rgba(255,255,255,.95);
  }
  .cover-logo-mark {
    width: 16px; height: 16px; border-radius: 50%;
    background: var(--brand-blue); flex: none;
  }
  .cover-logo-name {
    font-family: "Questrial", sans-serif; font-size: 23px; line-height: 1.1;
    color: var(--brand-blue);
  }
  .cover-intro {
    margin: 46px 34px 0; text-align: center; font-size: 17px; line-height: 1.45;
    font-family: "Open Sans", sans-serif; color: var(--ink-strong);
  }
  .cover-intro strong { font-weight: 700; }

  /* Back */
  .back { display: flex; flex-direction: column; font-family: "Open Sans", sans-serif; font-size: 15px; }
  .back-invite { margin-top: 70px; text-align: justify; }
  .back-contact { margin-top: auto; margin-bottom: 30px; }
  .back-contact-cta { margin-bottom: 18px; text-align: center; }
  .back-contact-line { font-weight: 700; display: flex; align-items: center; gap: 8px; }
  .back-contact-line svg { flex: none; }
</style>
</head>
<body>
<main class="canvas">

  <section class="spread spread--inside" aria-label="Brochure inside">
    <article class="panel">
      <h2 class="panel-title">Reasons To Outsource</h2>
      <div class="section">
        <h3 class="section-title">Time</h3>
        <p class="section-text">Outsourcing your accounting services will free up valuable time that can be spent on growing your practice. Bookkeeping, bill paying, payroll and other daily tasks can be taken off your plate from the very first month.</p>
      </div>
      <div class="section">
        <h3 class="section-title">Cost</h3>
        <p class="section-text">Firms often save as much as 25% compared with hiring in-house accounting staff, while gaining access to a full team of tax and advisory experts.</p>
      </div>
    </article>

    <article class="panel">
      <h2 class="panel-title">Our Commitment</h2>
      <div class="section">
        <h3 class="section-title">Excellence</h3>
        <p class="section-text">We strive to exceed your expectations as an accounting firm, by anticipating your financial needs and providing guidance throughout the year. Our staff are all licensed CPA's with experience in several industries so we are well-equipped to handle any complex accounting issues.</p>
      </div>
      <div class="section">
        <h3 class="section-title">Timeliness</h3>
        <p class="section-text">To make sound financial decisions, it is pertinent that records are maintained and analyzed monthly. We maintain your books on a monthly-basis, as well as calculate your estimated tax liability so there are no surprises at year-end.</p>
      </div>
    </article>

    <article class="panel">
      <div class="section">
        <h3 class="section-title">Advanced Tax Strategies</h3>
        <p class="section-text">Tax planning should be more than just finding out what you owe in advance. At Crestline Dental CPAs, we pride ourselves in advising in areas of advanced tax mitigation strategies, to reduce your overall tax bill - not just predict it.</p>
      </div>
      <div class="section">
        <h3 class="section-title">Personalization</h3>
        <p class="section-text">Every practice has different accounting needs, so we work closely with you to understand your specific financial and tax situations. Our services are tailored to guide you to meet your specific financial objectives.</p>
      </div>
    </article>
  </section>

  <section class="spread spread--outside" aria-label="Brochure outside">
    <article class="panel back">
      <p class="back-invite">Why not let us do the work? Schedule a free consultation and see how a clearer view of your finances can help your practice grow, so you can focus on your patients.</p>
      <div class="back-contact">
        <p class="back-contact-cta">Call or email us today to arrange your free review.</p>
        <p class="back-contact-line">
          <svg width="14" height="14" viewBox="0 0 24 24" aria-hidden="true"><path fill="#0a1014" d="M6.6 10.8a15 15 0 0 0 6.6 6.6l2.2-2.2a1 1 0 0 1 1-.25 11.4 11.4 0 0 0 3.6.57 1 1 0 0 1 1 1V20a1 1 0 0 1-1 1A17 17 0 0 1 3 4a1 1 0 0 1 1-1h3.5a1 1 0 0 1 1 1c0 1.25.2 2.45.57 3.57a1 1 0 0 1-.25 1z"/></svg>
          1-800-555-0142
        </p>
        <p class="back-contact-line">info@crestlinecpas.example</p>
      </div>
    </article>

    <article class="panel cover">
      <div class="cover-logo">
        <span class="cover-logo-mark" aria-hidden="true"></span>
        <span class="cover-logo-name">Crestline Dental CPAs Ltd.</span>
      </div>
      <p class="cover-intro">At <strong>Crestline Dental CPAs Ltd.</strong>, our licensed CPA's have the knowledge to tackle complex tax and accounting issues and the experience to present a clear picture of your financial position.</p>
    </article>
  </section>

</main>
</body>
</html>
```